Fresh pet feed direct from manufacturer to door step. Quality and Freshness un-surpassed in Industr

Need Business Card Design; leading into many other projects, for New Franchised Business Opportunity providing home delivery of fresh dog and cat feed (no emphasis needed for cat) direct from manufacturing facility. (no middle men or distributors) Food is Farm to Factory fresh. Our trademarked tagline is "Freshness is our FIRST Promise ! "
Updates

Please take note of other contest for Chirplane Cover and Profile Pic's

Target Market(s)

Dog and Cat owners

Industry/Entity Type

Pet

Contact Information for Business Card

Name, address, local phone, national 800 number, website, email address

Other font styles liked:
• follow that from logo

Requirements
Must have
• Our feed is made in Texas with ingredients sourced from local farms. We want to lean heavy on the Made in West Texas , ranch theme but that has a 'black label', 'vantrel', 'premium', 'high-end' look and feel
Nice to have
• maybe have an offer on card? 20% off with promo code "x" etc.. ?? just a thought...

```html
<!DOCTYPE html>
<html lang="en">
<head>
<meta charset="utf-8">
<title>Ridgecrest Premium – Business Card</title>
<link href="https://fonts.googleapis.com/css2?family=Ubuntu:wght@300;400;700&display=swap" rel="stylesheet">
<style>
  :root {
    --backdrop: #9c9c9c;
    --card-white: #f4f4f4;
    --card-shade: #e2e2e2;
    --ink-black: #0b0b0b;
    --gold: #b3861f;
    --text-light: #f2f2f2;
    --text-dark: #1a1a1a;
  }
  * { margin: 0; padding: 0; box-sizing: border-box; }
  html, body {
    width: 1200px; height: 720px; overflow: hidden;
    background: var(--backdrop);
    font-family: "Ubuntu", sans-serif;
  }
  .card {
    position: absolute; left: 100px; top: 75px;
    width: 1000px; height: 570px;
    background: linear-gradient(135deg, var(--card-white) 0%, var(--card-shade) 100%);
    overflow: hidden;
    box-shadow: 0 6px 18px rgba(0,0,0,0.25);
  }
  .card-shapes { position: absolute; inset: 0; }
  .brand {
    position: absolute; left: 190px; top: 70px;
    display: flex; align-items: center; gap: 16px;
  }
  .brand-dot {
    width: 46px; height: 46px; border-radius: 50%;
    background: var(--ink-black);
  }
  .brand-name {
    font-weight: 700; font-size: 40px; color: var(--ink-black);
    letter-spacing: 1px;
  }
  .tagline {
    position: absolute; left: 190px; top: 150px;
    font-size: 21px; color: var(--text-dark);
  }
  .contact {
    position: absolute; right: 60px; top: 330px;
    text-align: right; color: var(--text-light);
  }
  .person-name {
    font-weight: 700; font-size: 32px; line-height: 1.2;
    color: var(--gold); letter-spacing: 2px;
  }
  .person-role {
    font-weight: 300; font-size: 24px; line-height: 1.2;
    letter-spacing: 2px; margin-bottom: 8px;
  }
  .address {
    font-weight: 700; font-size: 19px; line-height: 1.3; margin-bottom: 8px;
  }
  .phone-line {
    display: flex; justify-content: flex-end; align-items: center; gap: 12px;
    font-weight: 300; font-size: 20px; letter-spacing: 1.5px; line-height: 1.5;
  }
  .phone-line svg { width: 18px; height: 18px; fill: var(--gold); flex: none; }
</style>
</head>
<body>
  <div class="card">
    <svg class="card-shapes" viewBox="0 0 1000 570" width="1000" height="570" aria-hidden="true">
      <path d="M-20 560 C 300 355, 650 262, 1010 270" fill="none" stroke="var(--gold)" stroke-width="9"/>
      <path d="M0 570 C 320 390, 660 305, 1000 318 L1000 570 Z" fill="var(--ink-black)"/>
    </svg>

    <div class="brand">
      <span class="brand-dot"></span>
      <span class="brand-name">RIDGECREST PREMIUM</span>
    </div>
    <p class="tagline">Freshness is our FIRST Promise !</p>

    <div class="contact">
      <p class="person-name">Dara Wellmont</p>
      <p class="person-role">Director</p>
      <p class="address">14/82 Mesa Road, Dun Flats,<br>Plain TX 410, Dun County TX 410</p>
      <p class="phone-line">1 800 555 014
        <svg viewBox="0 0 24 24" aria-label="phone"><path d="M6.6 10.8a15 15 0 0 0 6.6 6.6l2.2-2.2a1 1 0 0 1 1-.25 11.4 11.4 0 0 0 3.6.6 1 1 0 0 1 1 1V20a1 1 0 0 1-1 1A17 17 0 0 1 3 4a1 1 0 0 1 1-1h3.5a1 1 0 0 1 1 1c0 1.25.2 2.45.6 3.6a1 1 0 0 1-.25 1z"/></svg>
      </p>
      <p class="phone-line">07 5550 1288
        <svg viewBox="0 0 24 24" aria-label="fax"><path d="M6 2h12v6H6zM3 9h18a1 1 0 0 1 1 1v8h-4v4H6v-4H2v-8a1 1 0 0 1 1-1zm5 7v4h8v-4z"/></svg>
      </p>
      <p class="phone-line">04315550927
        <svg viewBox="0 0 24 24" aria-label="mobile"><path d="M7 1h10a2 2 0 0 1 2 2v18a2 2 0 0 1-2 2H7a2 2 0 0 1-2-2V3a2 2 0 0 1 2-2zm0 3v14h10V4z"/></svg>
      </p>
    </div>
  </div>
</body>
</html>
```